Book Cover "Venice"

Creation of a cover (14 x 20.5 cm + bleed area) for a book:
Image: “BrumeVerte” (Tiff joined)
AUTHOR: Maribel Quonte
TITLE: The murmurs of Oldmere
PUBLISHER: Editions Plavoc (AT THE BOTTOM OF THE COVER)
Updates

Target Market(s)

Readers of romantic novels

Industry/Entity Type

Book

```html
<!DOCTYPE html>
<html lang="en">
<head>
<meta charset="utf-8">
<title>The murmurs of Oldmere — Book Cover</title>
<link rel="stylesheet" href="https://fonts.googleapis.com/css2?family=Cormorant+Garamond:wght@600&family=Playfair+Display:wght@700&family=Lato:wght@400&display=swap">
<style>
  :root {
    --page-bg: #f2f1ef;
    --sky-top: #3c1220;
    --sky-deep: #8e1620;
    --sky-red: #c4241c;
    --sky-glow: #d63e1e;
    --dusk: #9a2219;
    --silhouette: #150b0e;
    --cream: #f7ecd2;
    --white: #ffffff;
  }
  * { margin: 0; padding: 0; box-sizing: border-box; }
  html, body {
    width: 1200px;
    height: 800px;
    overflow: hidden;
    background: var(--page-bg);
  }
  .stage {
    position: relative;
    width: 1200px;
    height: 800px;
  }
  .book-cover {
    position: absolute;
    left: 360px;
    top: 50px;
    width: 480px;
    height: 700px;
    overflow: hidden;
    box-shadow: 0 2px 10px rgba(0,0,0,0.15);
  }
  .cover-art {
    position: absolute;
    inset: 0;
    background:
      radial-gradient(ellipse 70% 30% at 50% 55%, rgba(230,80,40,0.55), transparent 70%),
      linear-gradient(180deg,
        var(--sky-top) 0%,
        var(--sky-deep) 14%,
        var(--sky-red) 34%,
        var(--sky-glow) 55%,
        var(--dusk) 72%,
        #4a1214 82%,
        var(--silhouette) 92%);
  }
  .author {
    position: absolute;
    top: 32px;
    width: 100%;
    text-align: center;
    font-family: "Cormorant Garamond", serif;
    font-weight: 600;
    font-size: 32px;
    letter-spacing: 0.5px;
    color: var(--cream);
  }
  .title {
    position: absolute;
    top: 150px;
    width: 100%;
    text-align: center;
    font-family: "Playfair Display", serif;
    font-weight: 700;
    color: var(--cream);
    text-shadow: 0 2px 6px rgba(60,0,0,0.35);
    line-height: 1;
  }
  .title-line-one {
    display: block;
    font-size: 62px;
    letter-spacing: -1px;
  }
  .title-line-two {
    display: block;
    margin-top: 4px;
    white-space: nowrap;
  }
  .title-small {
    font-size: 40px;
  }
  .title-large {
    font-size: 96px;
    letter-spacing: -2px;
  }
  .publisher {
    position: absolute;
    bottom: 18px;
    width: 100%;
    text-align: center;
    font-family: "Lato", sans-serif;
    font-size: 15px;
    color: var(--white);
  }
</style>
</head>
<body>
  <main class="stage">
    <section class="book-cover">
      <div class="cover-art" role="img" aria-label="Photograph of a blazing red sunset sky over the dark silhouette of domed city buildings and lit street lamps"></div>
      <p class="author">Maribel Quonte</p>
      <h1 class="title">
        <span class="title-line-one">The murmurs</span>
        <span class="title-line-two"><span class="title-small">of</span><span class="title-large">Oldmere</span></span>
      </h1>
      <p class="publisher">Editions Plavoc</p>
    </section>
  </main>
</body>
</html>
```